COBALT YARDS needs bisness cards pronto

Bisness name is "COBALT YARDS" new bisness the bisness includes lawn mowing, garden matanace, and any jobs around the house.
I need a card that is colorful and vibrant and the bisness of lawn mowing maybe with some nature with it. It also needs my contact details"Desmond Larkwell mobile 0412563049 call for free quote and email gwen.brookvale@fernmail.com and a catchy tag line

Requirements
Must have
• Bisness name "COBALT YARDS"
Contact details "0412563049"
Email gwen.brookvale@fernmail.com
Call for free quote

```html
<!DOCTYPE html>
<html lang="en">
<head>
<meta charset="utf-8">
<title>Cobalt Yards – Business Cards</title>
<link rel="stylesheet" href="https://fonts.googleapis.com/css2?family=Teko:wght@600&family=Oswald:wght@400;500&display=swap">
<style>
  :root {
    --page: #e6e6e6;
    --card-black: #050505;
    --grass-light: #6fc23a;
    --grass-mid: #3f9a24;
    --grass-dark: #2a7418;
    --brand-green: #8cc63f;
    --accent-red: #e2231a;
    --rule-blue: #3b4aa8;
    --photo-tone: #3f7fae;
  }
  * { margin: 0; padding: 0; box-sizing: border-box; }
  html, body { width: 1067px; height: 1200px; overflow: hidden; background: var(--page); }
  .canvas { position: relative; width: 1067px; height: 1200px; }

  .card {
    position: absolute;
    left: 103px;
    width: 860px;
    height: 492px;
    overflow: hidden;
    background: var(--card-black);
    box-shadow: 0 6px 18px rgba(0,0,0,.25);
  }
  .card--front { top: 70px; }
  .card--back { top: 638px; }

  .card__shapes { position: absolute; inset: 0; width: 100%; height: 100%; }

  .brand-name {
    font-family: "Teko", sans-serif;
    font-weight: 600;
    color: var(--brand-green);
    letter-spacing: 3px;
    line-height: 1;
    white-space: nowrap;
  }

  /* Front */
  .front__lockup {
    position: absolute;
    left: 0; right: 0;
    top: 168px;
    text-align: center;
  }
  .front__lockup .brand-name { font-size: 96px; }
  .front__tagline {
    font-family: "Oswald", sans-serif;
    font-weight: 500;
    font-size: 19px;
    color: var(--brand-green);
    letter-spacing: 1px;
    margin-top: 4px;
    display: flex;
    align-items: center;
    justify-content: center;
    gap: 14px;
  }
  .front__tagline .rule { width: 80px; height: 2px; background: var(--rule-blue); }

  /* Back */
  .back__details {
    position: absolute;
    left: 390px;
    top: 70px;
    width: 440px;
    font-family: "Oswald", sans-serif;
  }
  .back__details .brand-name { font-size: 72px; }
  .back__cta {
    font-weight: 500;
    font-size: 38px;
    color: var(--accent-red);
    margin-top: 14px;
    letter-spacing: 1px;
    white-space: nowrap;
  }
  .back__cta em { font-style: normal; color: var(--brand-green); }
  .back__rule { width: 300px; height: 2px; background: var(--rule-blue); margin: 8px 0 34px; }
  .back__person { font-size: 27px; color: var(--brand-green); text-transform: uppercase; letter-spacing: 1px; }
  .back__contact { font-size: 22px; color: var(--brand-green); margin-top: 12px; letter-spacing: 1px; white-space: nowrap; }
  .back__contact .label { color: var(--accent-red); margin-right: 6px; }
  .back__contact--email { text-transform: uppercase; font-size: 19px; margin-top: 6px; }
</style>
</head>
<body>
<div class="canvas">

  <section class="card card--front">
    <svg class="card__shapes" viewBox="0 0 860 492" preserveAspectRatio="none">
      <defs>
        <linearGradient id="grassFill" x1="0" y1="0" x2="0" y2="1">
          <stop offset="0" stop-color="var(--grass-light)"/>
          <stop offset=".5" stop-color="var(--grass-mid)"/>
          <stop offset="1" stop-color="var(--grass-dark)"/>
        </linearGradient>
      </defs>
      <g role="img" aria-label="Close-up lawn grass texture">
        <polygon fill="url(#grassFill)" points="0,0 860,0 860,128 820,138 790,126 760,142 720,130 690,150 650,134 610,146 560,132 520,150 470,136 430,152 380,140 330,156 290,138 250,150 200,134 160,148 120,132 70,146 30,134 0,142"/>
        <polygon fill="url(#grassFill)" points="0,352 40,342 80,358 130,340 170,356 220,344 270,362 320,346 360,360 410,342 460,356 500,340 550,358 600,344 650,362 700,346 750,358 800,342 860,354 860,492 0,492"/>
      </g>
    </svg>
    <div class="front__lockup">
      <div class="brand-name">COBALT YARDS</div>
      <div class="front__tagline"><span class="rule"></span>FOR YOUR PROFESSIONAL CUT LAWNS<span class="rule"></span></div>
    </div>
  </section>

  <section class="card card--back">
    <svg class="card__shapes" viewBox="0 0 860 492" preserveAspectRatio="none">
      <polygon role="img" aria-label="Photo of a gardener mowing a lawn" fill="var(--photo-tone)" points="0,0 300,0 292,40 312,80 296,120 318,160 300,200 322,240 304,280 326,320 308,360 330,400 312,440 334,492 0,492"/>
    </svg>
    <div class="back__details">
      <div class="brand-name">COBALT YARDS</div>
      <div class="back__cta">“CALL FOR <em>FREE QUOTE</em>”</div>
      <div class="back__rule"></div>
      <div class="back__person">Desmond Larkwell</div>
      <div class="back__contact"><span class="label">P:</span>0412563049</div>
      <div class="back__contact back__contact--email"><span class="label">E:</span>gwen.brookvale@fernmail.com</div>
    </div>
  </section>

</div>
</body>
</html>
```